An innovative, creative health promotion project needs you to add spice to logo and web design!

Wellorivan is “medical education for Asians”. We work with people from Indian, Pakistani, Bangladeshi and Sri Lankan backgrounds based in the UK. The aim is to use all of the great things we celebrate about Indian culture such as the vibrant colour, fashion, music, dance, Bollywood, cricket, tasty food and close family networks and use this to improve awareness about healthy living. Our tagline is “bright days with a little zest”. We are a group of healthcare professionals and creatives working in collaboration and we produce video interviews, local community events, blog posts and social media to address issues such as diabetes, heart disease, depression. We have 3 main subcategories – Mind, Movement and Meals. “Mind” addresses issues around mental illness through interviews with patients and healthcare professionals. “Movement” will get people more physically active through video and local group exercise and walking meetings. “Meals” will feature recipes from renowned Asian chefs to provide healthier alternatives. So far I have designed an amateur logo and we have a facebook page https://www.friendnook.example/wellorivan/ and a website hosted on wordpress: https://wellorivan.org/We are looking at help to create a simple but effective web design, logos and colour scheme that will capture the vibrant culture and give a feeling of energy, health and fun!

Target Market(s)

UK Indian community, all ages

Industry/Entity Type

Healthcare

Logo Text

bright days with a little zest

Number of Pages Required

1 page

Font styles to use
Sans Serif

Colors

Designer to choose colors to be used in the design.

Requirements
Must have
• Colour, vibrancy, energy, spice! fun!
Nice to have
• I would like clean design with ethnic colours.
Should not have
• No religious graphics

```html
<!DOCTYPE html>
<html lang="en">
<head>
<meta charset="utf-8">
<title>Wellorivan — bright days with a little zest</title>
<link href="https://fonts.googleapis.com/css2?family=Lato:wght@400;700;900&display=swap" rel="stylesheet">
<style>
:root{
  --maroon:#5b1129;
  --maroon-deep:#3e0a1c;
  --plum:#6d1a3a;
  --orange:#f26b12;
  --orange-soft:#f7a24e;
  --pink:#ead0de;
  --pink-bright:#f1b4ec;
  --lilac:#e2a6e6;
  --ink:#222;
  --grey:#666;
  --muted:#999;
  --white:#fff;
}
*{box-sizing:border-box;margin:0;padding:0}
html,body{width:1200px;height:3066px;overflow:hidden;background:var(--white);font-family:'Lato',Arial,sans-serif;color:var(--ink)}
.page{position:relative;width:1200px;height:3066px;overflow:hidden}
.abs{position:absolute}

/* header */
.site-header{position:absolute;left:0;top:0;width:1200px;height:96px;background:var(--white);z-index:5}
.brand{position:absolute;left:163px;top:20px}
.brand-name{font-weight:900;font-size:44px;line-height:44px;color:var(--maroon);letter-spacing:-1px}
.brand-tag{font-size:10px;color:var(--maroon);margin-left:36px;margin-top:2px}
.main-nav{position:absolute;left:480px;top:41px;display:flex;gap:30px;font-size:16px;color:#555}
.main-nav .active{color:var(--maroon)}

/* hero */
.hero{position:absolute;left:0;top:96px;width:1200px;height:590px;background:linear-gradient(180deg,#4d6a55 0%,#6e8a6a 30%,#8b7f6e 60%,#9b9a92 100%)}
.hero-title{position:absolute;left:0;top:318px;width:1200px;text-align:center;color:var(--white);font-weight:900;font-size:45px;line-height:50px;text-transform:uppercase}
.hero-arrow{position:absolute;top:322px}
.hero-wave{position:absolute;left:0;top:560px}

/* pillars */
.pillar{position:absolute;width:316px;height:316px;border-radius:50%;color:var(--white);text-align:center;z-index:3}
.pillar.mind,.pillar.meals{background:linear-gradient(180deg,#5e1430 0%,#3c0a1b 100%)}
.pillar.movement{background:linear-gradient(180deg,#f58a10 0%,#f04a18 100%)}
.pillar svg.icon{margin-top:40px}
.pillar h3{font-weight:400;font-size:27px;margin-top:8px}
.pillar p{font-size:15px;line-height:18px;margin:6px auto 0;width:220px}
.pillar .more{position:absolute;left:141px;bottom:20px}
.pillar.movement p{color:#ffe0b0}

/* about */
.issue-card{position:absolute;width:208px;height:196px;background:var(--white);border-radius:14px;box-shadow:0 6px 18px rgba(0,0,0,.12);text-align:center;z-index:2}
.issue-card svg{margin-top:20px}
.issue-card h4{font-weight:400;font-size:21px;color:var(--maroon);margin-top:6px}
.issue-card p{font-size:12px;line-height:15px;color:var(--muted);width:170px;margin:6px auto 0}
.about-title{position:absolute;left:593px;top:936px;font-weight:700;font-size:41px;color:var(--maroon)}
.about-copy{position:absolute;left:597px;top:1010px;width:440px;font-size:17px;line-height:26px;color:var(--grey)}
.btn{position:absolute;display:flex;align-items:center;justify-content:center;border:2px solid var(--orange);border-radius:26px;font-size:16px;font-weight:700;text-transform:uppercase;color:var(--maroon)}

/* blogs */
.section-title{position:absolute;left:0;width:1200px;text-align:center;font-weight:700;font-size:37px;color:var(--maroon)}
.blog-card{position:absolute;top:1545px;width:282px;height:321px;border:1px solid #ccc;background:var(--white);text-align:center}
.blog-photo{height:184px}
.blog-date{position:absolute;left:76px;top:164px;width:130px;height:28px;line-height:28px;background:var(--orange);color:var(--white);font-size:14px}
.blog-card h5{font-weight:400;font-size:17px;margin-top:24px}
.blog-card p{font-size:11px;line-height:15px;color:var(--grey);width:226px;margin:6px auto 0}
.blog-card .read{font-size:11px;font-weight:700;color:var(--maroon);margin-top:10px}

/* videos */
.video{position:absolute;top:2016px;height:296px}
.play{position:absolute;width:76px;height:76px;border-radius:50%;background:var(--white);display:flex;align-items:center;justify-content:center}

/* event */
.event-title{position:absolute;left:166px;top:2510px;font-weight:700;font-size:37px;color:var(--white)}
.event-copy{position:absolute;left:168px;top:2576px;width:420px;font-size:17px;line-height:26px;color:var(--white)}
.event-photo{position:absolute;left:589px;top:2490px;width:479px;height:288px;background:linear-gradient(180deg,#b8bcbf 0%,#6f6a6c 45%,#2c2428 100%);box-shadow:0 8px 18px rgba(0,0,0,.35)}

/* footer */
.footer-nav{position:absolute;left:0;top:2925px;width:1200px;display:flex;justify-content:center;gap:30px;font-size:17px;color:#333}
.copyright{position:absolute;left:0;top:2955px;width:1200px;text-align:center;font-size:14px;color:#666}
.social{position:absolute;top:3000px;display:flex;gap:8px;left:545px}
.social a{display:block;width:30px;height:30px;border-radius:50%;background:#2f63b0}
</style>
</head>
<body>
<div class="page">

  <header class="site-header">
    <div class="brand">
      <div class="brand-name">Wellorivan</div>
      <div class="brand-tag">health promotion with a little zest</div>
    </div>
    <nav class="main-nav">
      <span class="active">HOME</span><span>ABOUT US</span><span>BLOGS</span><span>SERVICES</span><span>ARTICLES</span><span>CONTACT</span>
    </nav>
  </header>

  <section class="hero" role="img" aria-label="Smiling man doing a push-up outdoors on a park path">
  </section>
  <h1 class="hero-title">Bright days with<br>a little zest</h1>
  <svg class="hero-arrow" style="left:128px" width="32" height="60" viewBox="0 0 32 60"><path d="M28 4 L4 30 L28 56" fill="none" stroke="#fff" stroke-width="3"/></svg>
  <svg class="hero-arrow" style="left:1044px" width="32" height="60" viewBox="0 0 32 60"><path d="M4 4 L28 30 L4 56" fill="none" stroke="#fff" stroke-width="3"/></svg>
  <svg class="hero-wave" width="1200" height="140" viewBox="0 0 1200 140" preserveAspectRatio="none">
    <path d="M0 70 C250 130 450 30 700 40 C900 48 1050 20 1200 60 L1200 140 L0 140 Z" fill="#fff"/>
  </svg>

  <!-- pillars -->
  <div class="pillar mind" style="left:159px;top:493px">
    <svg class="icon" width="64" height="72" viewBox="0 0 64 72" fill="none" stroke="#fff" stroke-width="2.5"><path d="M20 68 V52 C8 46 4 34 8 22 C12 8 26 2 38 4 C52 6 60 18 58 32 L62 42 L56 44 V52 C56 58 50 58 44 58 V68"/><circle cx="34" cy="26" r="10" stroke-dasharray="3 3"/></svg>
    <h3>Mind</h3>
    <p>Addresses issues around mental illness through interviews with patients and healthcare professionals</p>
    <svg class="more" width="34" height="34" viewBox="0 0 34 34"><circle cx="17" cy="17" r="15" fill="none" stroke="#fff" stroke-width="2"/><path d="M11 14 L17 20 L23 14" fill="none" stroke="#fff" stroke-width="2"/></svg>
  </div>
  <div class="pillar movement" style="left:449px;top:493px">
    <svg class="icon" width="64" height="72" viewBox="0 0 64 72" fill="none" stroke="#fff" stroke-width="3"><circle cx="32" cy="12" r="7"/><path d="M8 8 L22 26 H42 L56 8 M24 26 L26 44 L18 66 M40 26 L38 44 L46 66 M14 40 H50"/></svg>
    <h3>Movement</h3>
    <p>will get people more physically active through video and local group exercise and walking meetings</p>
    <svg class="more" width="34" height="34" viewBox="0 0 34 34"><circle cx="17" cy="17" r="15" fill="none" stroke="#fff" stroke-width="2"/><path d="M11 14 L17 20 L23 14" fill="none" stroke="#fff" stroke-width="2"/></svg>
  </div>
  <div class="pillar meals" style="left:735px;top:493px">
    <svg class="icon" width="76" height="72" viewBox="0 0 76 72" fill="none" stroke="#fff" stroke-width="2.5"><circle cx="38" cy="36" r="20"/><circle cx="38" cy="36" r="12"/><path d="M6 8 V28 M12 8 V28 M18 8 V28 M6 28 H18 M12 28 V66 M64 8 C72 18 72 34 64 38 V66"/></svg>
    <h3>Meals</h3>
    <p>will feature recipes from renowned Asian chefs to provide healthier alternatives.</p>
    <svg class="more" width="34" height="34" viewBox="0 0 34 34"><circle cx="17" cy="17" r="15" fill="none" stroke="#fff" stroke-width="2"/><path d="M11 14 L17 20 L23 14" fill="none" stroke="#fff" stroke-width="2"/></svg>
  </div>

  <!-- about -->
  <svg class="abs" style="left:0;top:800px" width="600" height="670" viewBox="0 0 600 670">
    <path d="M0 30 C120 10 260 -10 330 40 C420 100 520 160 560 260 C600 360 520 460 440 540 C360 620 200 660 60 640 L0 650 Z" fill="#f5d3f0"/>
    <path d="M0 110 C140 80 260 60 330 120 C410 190 470 280 470 360 C470 450 380 530 280 580 C190 620 100 630 0 620 Z" fill="var(--pink-bright)"/>
    <path d="M0 200 C110 170 220 190 280 260 C330 330 320 420 260 490 C200 560 110 590 0 580 Z" fill="#d98fd9"/>
    <path d="M0 250 C80 230 150 260 170 330 C190 410 150 490 80 530 C50 545 20 550 0 550 Z" fill="#7a1a1a"/>
  </svg>

  <div class="issue-card" style="left:160px;top:886px">
    <svg width="44" height="58" viewBox="0 0 44 58" fill="none" stroke="var(--orange)" stroke-width="2.5"><rect x="4" y="4" width="36" height="44" rx="6"/><rect x="10" y="10" width="24" height="14"/><path d="M16 48 V56 H28 V48 M12 32 H32 M12 38 H32"/></svg>
    <h4>Daiabetes</h4>
    <p>Class aptent taciti soc iosqu ad litora torquent per conu</p>
  </div>
  <div class="issue-card" style="left:333px;top:1023px">
    <svg width="50" height="56" viewBox="0 0 50 56" fill="none" stroke="var(--orange)" stroke-width="2.5"><path d="M14 54 V42 C4 36 2 24 6 14 C10 4 22 0 32 2 C44 4 50 16 46 28 L48 36 L44 38 V44 H36 V54"/><circle cx="26" cy="22" r="8"/></svg>
    <h4>Depression</h4>
    <p>Class aptent taciti soc iosqu ad litora torquent per conu</p>
  </div>
  <div class="issue-card" style="left:160px;top:1141px">
    <svg width="64" height="56" viewBox="0 0 64 56" fill="none" stroke="var(--orange)" stroke-width="2.5"><path d="M32 52 L8 28 C0 20 2 6 14 4 C22 2 28 8 32 14 C36 8 42 2 50 4 C62 6 64 20 56 28 Z"/><path d="M4 28 H20 L26 18 L32 38 L38 24 L42 28 H60"/></svg>
    <h4>Heart Disease</h4>
    <p>Class aptent taciti soc iosqu ad litora torquent per conu</p>
  </div>

  <h2 class="about-title">About Wellorivan</h2>
  <p class="about-copy">Wellorivan is “medical education for Asians”. We work with people from Indian, Pakistani, Bangladeshi and Sri Lankan backgrounds based in the UK. The aim is to use all of the great things we celebrate about Indian culture such as the vibrant colour, fashion, music, dance, Bollywood, cricket, tasty food and close family networks and use this to improve awareness about healthy living</p>
  <div class="btn" style="left:597px;top:1223px;width:170px;height:51px">Learn More</div>

  <!-- blogs -->
  <h2 class="section-title" style="top:1463px">Recent Blogs</h2>
  <article class="blog-card" style="left:160px">
    <div class="blog-photo" role="img" aria-label="Community group seated at tables during a workshop" style="background:linear-gradient(180deg,#d8d4cf,#6e6662)"></div>
    <div class="blog-date">05 Jan 2019</div>
    <h5>Your Blog Title here</h5>
    <p>netus et malesuada fames ac turpis egestas Cras id elit Integer quis urna Ut ante enim dapibus malesuada fringilla eu cond</p>
    <div class="read">READ MORE</div>
  </article>
  <article class="blog-card" style="left:464px">
    <div class="blog-photo" role="img" aria-label="Group of volunteers standing together outdoors" style="background:linear-gradient(180deg,#3d6fc4 0%,#6fa0d8 35%,#4f6b3a 100%)"></div>
    <div class="blog-date">02 Dec 2018</div>
    <h5>Your Blog Title here</h5>
    <p>netus et malesuada fames ac turpis egestas Cras id elit Integer quis urna Ut ante enim dapibus malesuada fringilla eu cond</p>
    <div class="read">READ MORE</div>
  </article>
  <article class="blog-card" style="left:767px">
    <div class="blog-photo" role="img" aria-label="Smiling group of walkers posing together" style="background:linear-gradient(180deg,#c9c4be,#5a4a52 60%,#2a2226)"></div>
    <div class="blog-date">10 Dec 2018</div>
    <h5>Your Blog Title here</h5>
    <p>netus et malesuada fames ac turpis egestas Cras id elit Integer quis urna Ut ante enim dapibus malesuada fringilla eu cond</p>
    <div class="read">READ MORE</div>
  </article>

  <!-- videos band -->
  <svg class="abs" style="left:0;top:1890px" width="1200" height="540" viewBox="0 0 1200 540" preserveAspectRatio="none">
    <path d="M0 70 C300 20 700 0 900 10 C1050 18 1150 40 1200 60 L1200 500 L0 500 Z" fill="var(--orange-soft)"/>
    <path d="M0 80 C300 30 700 10 900 22 C1050 30 1150 55 1200 80 L1200 500 L0 500 Z" fill="var(--pink)"/>
  </svg>
  <h2 class="section-title" style="top:1935px">Our Videos</h2>
  <div class="video" style="left:164px;width:425px" role="img" aria-label="Video still of a community discussion group around tables">
    <div style="position:absolute;inset:0;background:linear-gradient(180deg,#e6e4e0,#8f8a86 55%,#3a3330)"></div>
    <div class="play" style="left:174px;top:110px"><svg width="28" height="32" viewBox="0 0 28 32"><path d="M4 2 L26 16 L4 30 Z" fill="#111"/></svg></div>
  </div>
  <div class="video" style="left:609px;width:428px" role="img" aria-label="Video still of a presenter speaking beside a projected slide">
    <div style="position:absolute;inset:0;background:linear-gradient(180deg,#8a7d70,#5a5048 50%,#2c2622)"></div>
    <div class="play" style="left:176px;top:110px"><svg width="28" height="32" viewBox="0 0 28 32"><path d="M4 2 L26 16 L4 30 Z" fill="#111"/></svg></div>
  </div>

  <!-- event band -->
  <svg class="abs" style="left:0;top:2340px" width="1200" height="540" viewBox="0 0 1200 540" preserveAspectRatio="none">
    <path d="M0 30 C250 60 600 80 900 70 C1050 64 1150 50 1200 40 L1200 540 L0 540 Z" fill="#b8461c"/>
    <path d="M0 48 C250 74 600 92 900 84 C1050 78 1150 64 1200 54 L1200 540 L0 540 Z" fill="var(--maroon)"/>
  </svg>
  <h2 class="event-title">Local Community Event</h2>
  <p class="event-copy">Vivamus porttitor purus nisi eleifend libero a tempus libero lectus feugiat felis Morbi diam mauris viverra in gravida eu mattis in ante Morbi eget arcu Morbi porta libero id ullamcorper nonummy nibh ligula pulvinar metus eget consectetuer augue nisi quis .</p>
  <div class="btn" style="left:168px;top:2738px;width:169px;height:49px;color:var(--white)">Learn More</div>
  <div class="event-photo" role="img" aria-label="Large group photo of community members outdoors in winter"></div>

  <!-- footer -->
  <nav class="footer-nav"><span>HOME</span><span>ABOUT US</span><span>BLOGS</span><span>SERVICES</span><span>ARTICLES</span><span>CONTACT</span></nav>
  <p class="copyright">© 2019 Company Name  All right reserved</p>
  <div class="social">
    <a href="https://www.friendnook.example/wellorivan/" aria-label="Wellorivan on FriendNook"></a>
    <a aria-label="Social profile"></a>
    <a aria-label="Social profile"></a>
  </div>

</div>
</body>
</html>
```